New Business Card Design Project

Want a simple but attention grabbing business card. Back Side having mainly our logo and basic info-the front side a typical business card.

Contact Information for Business Card

Hearth & Tile Interiors
218 NW Larkspur Rd. Suite 207
Cedar Hollow, Ohio 43017

phone- 614.482.7093

website is -htidesigns.com

```html
<!DOCTYPE html>
<html lang="en">
<head>
<meta charset="utf-8">
<title>Hearth &amp; Tile Interiors – Business Card</title>
<link rel="stylesheet" href="https://fonts.googleapis.com/css2?family=Montserrat:wght@500;600;700&display=swap">
<style>
  :root {
    --brand-blue: #2979ff;
    --brand-red: #ff3d14;
    --paper: #ffffff;
    --page: #ffffff;
    --shadow: rgba(0, 0, 0, 0.28);
  }
  * { box-sizing: border-box; margin: 0; padding: 0; }
  html, body {
    width: 1200px;
    height: 1000px;
    overflow: hidden;
    background: var(--page);
    font-family: "Montserrat", Arial, sans-serif;
  }
  .canvas {
    position: relative;
    width: 1200px;
    height: 1000px;
  }
  .card {
    position: absolute;
    left: 222px;
    width: 757px;
    height: 432px;
    box-shadow: 3px 4px 8px var(--shadow);
  }
  .card--back {
    top: 46px;
    background: var(--brand-blue);
    display: flex;
    align-items: center;
    justify-content: center;
  }
  .card--front {
    top: 522px;
    background: var(--paper);
  }

  /* Stacked company wordmark: square, name, descriptor line */
  .wordmark {
    display: flex;
    flex-direction: column;
    align-items: center;
    font-weight: 700;
    text-transform: uppercase;
    white-space: nowrap;
    line-height: 1;
  }
  .wordmark__square {
    background: currentColor;
    flex: none;
  }
  .wordmark__name { letter-spacing: 0.01em; }
  .wordmark__descriptor { letter-spacing: 0.9em; margin-right: -0.9em; }

  .card--back .wordmark { color: var(--paper); margin-top: 4px; }
  .card--back .wordmark__square { width: 24px; height: 24px; margin-bottom: 30px; }
  .card--back .wordmark__name { font-size: 56px; }
  .card--back .wordmark__descriptor { font-size: 18px; margin-top: 18px; }

  .card--front .wordmark {
    position: absolute;
    right: 52px;
    top: 62px;
    width: 304px;
    color: var(--brand-red);
  }
  .card--front .wordmark__square { width: 14px; height: 14px; margin-bottom: 18px; }
  .card--front .wordmark__name { font-size: 33px; }
  .card--front .wordmark__descriptor { font-size: 11px; margin-top: 10px; }

  .person {
    position: absolute;
    left: 55px;
    top: 240px;
  }
  .person__name {
    color: var(--brand-red);
    font-size: 38px;
    font-weight: 700;
    line-height: 1;
  }
  .person__role {
    color: var(--brand-blue);
    font-size: 18px;
    font-weight: 600;
    margin-top: 4px;
    margin-left: 3px;
  }
  .address {
    position: absolute;
    left: 55px;
    top: 330px;
    color: var(--brand-blue);
    font-size: 18px;
    font-weight: 500;
    line-height: 22px;
    font-style: normal;
  }
  .contact {
    position: absolute;
    right: 53px;
    top: 312px;
    text-align: right;
  }
  .contact__phone {
    color: var(--brand-blue);
    font-size: 30px;
    font-weight: 700;
    line-height: 1;
  }
  .contact__web {
    color: var(--brand-red);
    font-size: 17px;
    font-weight: 700;
    margin-top: 14px;
  }
</style>
</head>
<body>
<main class="canvas">
  <section class="card card--back" aria-label="Card back">
    <div class="wordmark">
      <span class="wordmark__square"></span>
      <span class="wordmark__name">Hearth &amp; Tile</span>
      <span class="wordmark__descriptor">Interiors</span>
    </div>
  </section>

  <section class="card card--front" aria-label="Card front">
    <div class="wordmark">
      <span class="wordmark__square"></span>
      <span class="wordmark__name">Hearth &amp; Tile</span>
      <span class="wordmark__descriptor">Interiors</span>
    </div>

    <div class="person">
      <p class="person__name">EXAMPLE NAME</p>
      <p class="person__role">Director</p>
    </div>

    <address class="address">
      218 NW Larkspur Rd. Suite 207<br>
      Cedar Hollow, Ohio 43017
    </address>

    <div class="contact">
      <p class="contact__phone">614.482.7093</p>
      <p class="contact__web">www.htidesigns.com</p>
    </div>
  </section>
</main>
</body>
</html>
```